VELU Medical Spa

We'd like a business card with the reverse of the card for appointments. We like round corners and vertical design. We have a background image and bird logo to include with the following wording on the front:-
Velu Medical Spa
248 Pembury Street
NORTH ADELAIDE
SA 5006
Phone 08 83915746
www.velumedicalspa.com.au
Facebook velumedicalspa
Instagram velumedicalspa
On the back I'd like an appointment card layout please.
Cheers Dee

```html
<!DOCTYPE html>
<html lang="en">
<head>
<meta charset="utf-8">
<title>VELU Medical Spa – Business &amp; Appointment Card</title>
<link rel="stylesheet" href="https://fonts.googleapis.com/css2?family=Cormorant+Garamond:wght@500&family=Poppins:wght@400;500&display=swap">
<style>
  :root {
    --stage: #3a3a3a;
    --mint: #a9dcc0;
    --mint-light: #b7e6cd;
    --teal: #7ccbc2;
    --teal-deep: #6fbfba;
    --ink: #111111;
    --white: #ffffff;
  }
  * { box-sizing: border-box; margin: 0; padding: 0; }
  html, body { width: 1200px; height: 900px; overflow: hidden; }
  body {
    background: var(--stage);
    position: relative;
    font-family: "Poppins", sans-serif;
    color: var(--ink);
  }
  .card {
    position: absolute;
    border-radius: 22px;
    overflow: hidden;
  }

  /* Front: vertical contact card */
  .card-front {
    left: 110px; top: 150px;
    width: 350px; height: 600px;
    background: var(--mint);
    display: flex; flex-direction: column; align-items: center;
    text-align: center;
    padding-top: 110px;
  }
  .brand-mark {
    display: flex; align-items: center; gap: 12px;
    margin-bottom: 60px;
  }
  .brand-dot {
    width: 34px; height: 34px; border-radius: 50%;
    background: var(--ink);
    flex: none;
  }
  .brand-name {
    font-family: "Poppins", sans-serif;
    font-weight: 500;
    font-size: 26px;
    color: var(--ink);
    line-height: 1;
  }
  .address {
    font-size: 19px; font-weight: 500; line-height: 1.15;
  }
  .contact-icons {
    display: flex; gap: 8px; margin: 22px 0 10px;
  }
  .icon {
    width: 24px; height: 24px; border-radius: 50%;
    background: var(--ink);
    display: flex; align-items: center; justify-content: center;
  }
  .phone { font-size: 19px; font-weight: 500; }
  .web { font-size: 19px; font-weight: 500; margin-top: 34px; }
  .social {
    display: flex; align-items: center; gap: 6px;
    margin-top: 20px; font-size: 19px; font-weight: 500;
  }
  .social-dot { width: 24px; height: 24px; border-radius: 50%; background: var(--ink); }

  /* Back: horizontal appointment card */
  .card-back {
    left: 520px; top: 280px;
    width: 600px; height: 345px;
    background: linear-gradient(135deg, var(--mint-light) 0%, var(--mint) 35%, var(--teal) 100%);
  }
  .foliage {
    position: absolute; left: 90px; top: 40px; width: 510px; height: 305px;
    background: radial-gradient(ellipse at 55% 60%, rgba(111,191,186,0.85) 0%, rgba(124,203,194,0.5) 45%, rgba(169,220,192,0) 75%);
  }
  .spa-title {
    position: absolute; right: 36px; top: 30px;
    border: 1.5px solid var(--ink);
    padding: 8px 22px;
    font-family: "Cormorant Garamond", serif;
    font-weight: 500; font-size: 34px; letter-spacing: 1px;
  }
  .appointment {
    position: absolute; left: 36px; top: 110px;
    font-size: 14px; letter-spacing: 0.5px;
  }
  .appointment-row { display: flex; align-items: flex-end; margin-bottom: 22px; }
  .appointment-label { font-weight: 500; white-space: nowrap; }
  .days { margin-left: 10px; word-spacing: 4px; }
  .fill-line { border-bottom: 1.5px solid var(--ink); margin-left: 10px; height: 1px; }
  .fill-date { width: 230px; }
  .fill-time { width: 240px; }
  .ampm { margin-left: 14px; }
</style>
</head>
<body>

  <section class="card card-front" aria-label="Business card front">
    <div class="brand-mark">
      <span class="brand-dot"></span>
      <span class="brand-name">VELU Medical Spa</span>
    </div>
    <p class="address">248 Pembury Street<br>NORTH ADELAIDE<br>SA 5006</p>
    <div class="contact-icons">
      <span class="icon">
        <svg width="12" height="12" viewBox="0 0 24 24"><path fill="#fff" d="M6.6 10.8a15 15 0 0 0 6.6 6.6l2.2-2.2c.3-.3.7-.4 1-.2 1.1.4 2.3.6 3.6.6.6 0 1 .4 1 1V20c0 .6-.4 1-1 1A17 17 0 0 1 3 4c0-.6.4-1 1-1h3.5c.6 0 1 .4 1 1 0 1.3.2 2.5.6 3.6.1.3 0 .7-.2 1z"/></svg>
      </span>
      <span class="icon">
        <svg width="14" height="14" viewBox="0 0 24 24" fill="none" stroke="#fff" stroke-width="2"><circle cx="12" cy="12" r="9"/><path d="M3 12h18M12 3c3 3 3 15 0 18M12 3c-3 3-3 15 0 18"/></svg>
      </span>
    </div>
    <p class="phone">08 83915746</p>
    <p class="web">www.velumedicalspa.com.au</p>
    <div class="social">
      <span class="social-dot"></span>
      <span class="social-dot"></span>
      <span>velumedicalspa</span>
    </div>
  </section>

  <section class="card card-back" aria-label="Appointment card back">
    <div class="foliage" role="img" aria-label="Soft palm leaf background in pale teal"></div>
    <h1 class="spa-title">VELU MEDICAL SPA</h1>
    <div class="appointment">
      <div class="appointment-row">
        <span class="appointment-label">APPOINMENT ON :</span>
        <span class="days">Sa / Su / Mo / Tu / We / Th / Fr</span>
      </div>
      <div class="appointment-row">
        <span class="appointment-label">DATE :</span>
        <span class="fill-line fill-date"></span>
      </div>
      <div class="appointment-row">
        <span class="appointment-label">TIME :</span>
        <span class="fill-line fill-time"></span>
        <span class="ampm">AM / PM</span>
      </div>
    </div>
  </section>

</body>
</html>
```